brolvix new business card design project

we need a new business card design. you can view info about us @ brolvix.example. i have attached an example of our previous card with our previous name that we no longer use. We really liked the design, colors etc. look below to see more info about this project. it asks for a limited number of words. please see our website for more info about our compnay.

Target Market(s)

law enforcement

Contact Information for Business Card

i have uploaded an example of what we used before that we liked.

Font styles to use
Serif

```html
<!DOCTYPE html>
<html lang="en">
<head>
<meta charset="utf-8">
<title>Brolvix Business Card</title>
<link href="https://fonts.googleapis.com/css2?family=Lato:wght@300;400;700;900&display=swap" rel="stylesheet">
<style>
  :root {
    --backdrop: #9e9e9e;
    --card-front: #0c1b25;
    --card-back-deep: #0d2232;
    --card-back-mid: #16384f;
    --ink-white: #ffffff;
    --ink-soft: #c9d2d8;
  }
  html, body {
    margin: 0;
    padding: 0;
    width: 1200px;
    height: 900px;
    overflow: hidden;
    background: var(--backdrop);
    font-family: "Lato", Arial, sans-serif;
  }
  .stage {
    position: relative;
    width: 1200px;
    height: 900px;
  }
  .card {
    position: absolute;
    top: 200px;
    width: 310px;
    height: 502px;
    overflow: hidden;
    color: var(--ink-white);
  }
  .card--front {
    left: 253px;
    background: var(--card-front);
    border-radius: 50px 0 50px 0;
  }
  .card--back {
    left: 627px;
    border-radius: 0 50px 0 50px;
  }
  .network-field {
    position: absolute;
    inset: 0;
    background:
      radial-gradient(ellipse at 80% 30%, var(--card-back-mid) 0%, transparent 60%),
      linear-gradient(180deg, var(--card-back-mid) 0%, var(--card-back-deep) 55%, #0b1d2b 100%);
  }
  .wordmark {
    position: absolute;
    left: 0;
    right: 0;
    text-align: center;
    font-weight: 300;
    font-size: 46px;
    letter-spacing: 3px;
    line-height: 1;
    color: var(--ink-white);
  }
  .card--front .wordmark { top: 148px; }
  .card--back .wordmark { top: 166px; }
  .tagline {
    position: absolute;
    top: 228px;
    left: 0;
    right: 0;
    text-align: center;
    font-weight: 700;
    font-size: 14px;
    letter-spacing: 0.3px;
  }
  .holder {
    position: absolute;
    left: 33px;
    top: 299px;
  }
  .holder__name {
    font-weight: 900;
    font-size: 16px;
    letter-spacing: 0.6px;
    line-height: 20px;
  }
  .holder__role {
    font-size: 14px;
    color: var(--ink-soft);
    line-height: 17px;
  }
  .contact {
    position: absolute;
    left: 32px;
    top: 348px;
    margin: 0;
    padding: 0;
    list-style: none;
    font-size: 14px;
    color: var(--ink-soft);
  }
  .contact li {
    display: flex;
    align-items: center;
    height: 18px;
  }
  .contact svg {
    width: 11px;
    height: 11px;
    margin-right: 6px;
    fill: var(--ink-soft);
  }
  .address {
    position: absolute;
    left: 34px;
    top: 420px;
    margin: 0;
    font-style: normal;
    font-size: 14px;
    line-height: 18px;
    color: var(--ink-soft);
  }
  .services {
    position: absolute;
    top: 388px;
    left: 0;
    right: 0;
    margin: 0;
    padding: 0;
    list-style: none;
    text-align: center;
    font-size: 14.5px;
    line-height: 23px;
    letter-spacing: 0.2px;
  }
</style>
</head>
<body>
<main class="stage">
  <section class="card card--front" aria-label="Business card front">
    <div class="wordmark">BROLVIX</div>
    <div class="holder">
      <div class="holder__name">DANIEL HARPER</div>
      <div class="holder__role">Managing Director</div>
    </div>
    <ul class="contact">
      <li><svg viewBox="0 0 12 12" aria-hidden="true"><path d="M1 4c0-2 2-3 5-3s5 1 5 3l-2 .6L8 3H4L3 4.6zM3 5h6l2 5H1z"/></svg>866.555.0142</li>
      <li><svg viewBox="0 0 12 12" aria-hidden="true"><path d="M0 2h12v8H0zM1 3v.5l5 3.2 5-3.2V3z"/></svg>info@brolvix.example</li>
      <li><svg viewBox="0 0 12 12" aria-hidden="true"><circle cx="6" cy="6" r="5.5"/></svg>www.brolvix.example</li>
    </ul>
    <address class="address">4180 Ridgeline Avenue<br>Austin, TX 78731</address>
  </section>

  <section class="card card--back" aria-label="Business card back">
    <div class="network-field" role="img" aria-label="Dark blue connected-node network pattern"></div>
    <div class="wordmark">BROLVIX</div>
    <div class="tagline">LAW ENFORCEMENT INNOVATION</div>
    <ul class="services">
      <li>LAW ENFORCEMENT</li>
      <li>JUSTICE OF THE PEACE</li>
      <li>MUNICIPAL COURTS</li>
    </ul>
  </section>
</main>
</body>
</html>
```